Fern and Slate Mobile Bartending Website

Looking for an informational website for our mobile bartending business. We want to include features we like from another website that will help support our business.

Something with a similar set-up to https://velvetfinchpours.com/

```html
<!DOCTYPE html>
<html lang="en">
<head>
<meta charset="utf-8">
<title>Fern &amp; Slate – Mobile Bartending</title>
<link href="https://fonts.googleapis.com/css2?family=Roboto:wght@400;500;700&display=swap" rel="stylesheet">
<style>
:root{
  --brown:#6b4300;
  --tan:#f8d896;
  --tan-soft:#f7dd9c;
  --ink:#111111;
  --text:#555555;
  --white:#ffffff;
  --black:#000000;
  --field:#ffffff;
}
*{margin:0;padding:0;box-sizing:border-box}
html,body{width:1200px;height:4055px;overflow:hidden;background:var(--white)}
body{position:relative;font-family:'Roboto',Arial,sans-serif;color:var(--ink)}
.abs{position:absolute}
a{color:inherit}
.btn{position:absolute;display:flex;align-items:center;justify-content:center;border-radius:24px;font-size:15px;font-weight:500;text-decoration:none}
.btn-dark{background:var(--brown);color:var(--white)}
.btn-light{background:var(--tan);color:var(--brown)}
.btn-outline{border:2px solid var(--brown);color:var(--brown)}

.top-line{left:0;top:0;width:1200px;height:4px;background:var(--tan)}
.hero-photo{left:0;top:4px;width:1200px;height:724px;background:linear-gradient(160deg,#f3f3f0 0%,#d9d5cc 18%,#b33a32 32%,#9c2b26 50%,#8d7c60 75%,#d6c4a0 100%)}
.header-fade{left:0;top:4px;width:1200px;height:140px;background:linear-gradient(#f5f5f3 55%,rgba(245,245,243,0))}
.brand{font-weight:500;letter-spacing:1px;white-space:nowrap}
.logo-head{left:110px;top:70px;font-size:30px;color:var(--ink)}
.nav{top:91px;font-size:15px;font-weight:500;color:var(--ink)}

.hero-ring{left:645px;top:175px;width:470px;height:470px;border-radius:50%;background:rgba(160,125,60,.75)}
.hero-circle{left:667px;top:211px;width:414px;height:414px;border-radius:50%;background:var(--brown)}
.hero-text{left:667px;width:414px;text-align:center;color:var(--white)}

.mark{width:22px;height:22px;border-radius:50%;background:var(--ink);left:589px}
.section-title{left:0;width:1200px;text-align:center;font-size:40px;font-weight:700;color:var(--ink)}
.about-col{top:990px;width:453px;font-size:13.5px;line-height:29px;color:var(--text)}

.van-photo{left:0;top:1310px;width:1200px;height:570px;background:linear-gradient(#ffffff 0%,#eef0ee 12%,#d9a72f 35%,#e8b23a 60%,#c9b28a 82%,var(--tan) 100%)}
.serve-bg{left:0;top:1878px;width:1200px;height:1000px;background:var(--tan)}
.card{top:2168px;width:304px;height:500px;background:var(--white);border-radius:152px 152px 150px 150px;text-align:center}
.card-photo{position:absolute;left:11px;top:12px;width:282px;height:282px;border-radius:50%}
.card h3{position:absolute;top:324px;width:100%;font-size:20px;font-weight:500;color:var(--brown)}
.card p{position:absolute;top:358px;left:30px;width:244px;font-size:13.5px;line-height:23px;color:var(--text)}
.card a{position:absolute;top:440px;left:0;width:100%;font-size:14px;font-weight:500;color:var(--brown)}

.info-icon{left:133px;width:44px;height:44px;border-radius:50%;background:var(--brown)}
.info-title{left:198px;font-size:17px;font-weight:700}
.info-text{left:198px;font-size:13.5px;line-height:27px;color:var(--text)}
.field{background:var(--field);box-shadow:0 0 0 1px #f0f0f0;font-size:13.5px;color:#777;padding:21px 24px 0}
.social{width:44px;height:44px;border-radius:50%;background:var(--white);display:flex;align-items:center;justify-content:center;box-shadow:0 2px 8px rgba(0,0,0,.12)}

.footer-bg{left:0;top:3560px;width:1200px;height:495px}
.foot-nav{top:3888px;font-size:15px;font-weight:500;color:var(--white)}
</style>
</head>
<body>

<div class="abs top-line"></div>

<!-- Hero -->
<div class="abs hero-photo" role="img" aria-label="Red vintage bartending trailer with a smiling host at the serving window, outdoors"></div>
<div class="abs header-fade"></div>
<div class="abs brand logo-head">FERN &amp; SLATE</div>
<a class="btn btn-dark" style="left:770px;top:28px;width:136px;height:42px">Get Started</a>
<a class="btn btn-light" style="left:926px;top:28px;width:163px;height:42px">Schedule Consult</a>
<div class="abs nav" style="left:517px">Home</div>
<div class="abs nav" style="left:619px">About Us</div>
<div class="abs nav" style="left:744px">Our Services</div>
<div class="abs nav" style="left:894px">Reviews</div>
<div class="abs nav" style="left:1013px">Contact Us</div>

<div class="abs hero-ring"></div>
<div class="abs hero-circle"></div>
<div class="abs hero-text" style="top:340px;font-size:40px;font-weight:500">Welcome To</div>
<div class="abs hero-text" style="top:390px;font-size:58px;font-weight:500">Fern &amp; Slate</div>
<div class="abs hero-text" style="top:478px;font-size:19px;font-weight:500">MOBILE BARTENDING</div>
<a class="btn btn-light" style="left:806px;top:533px;width:136px;height:44px">Get Started</a>

<!-- About -->
<div class="abs mark" style="top:848px"></div>
<h2 class="abs section-title" style="top:915px">ABOUT FERN &amp; SLATE</h2>
<p class="abs about-col" style="left:125px;text-align:right">On the other hand, we denounce with righteous indignation and dislike men who are so beguiled and demoralized by the charms of pleasure of the moment, so blinded by desire, that they cannot foresee the pain and trouble that are bound to ensue; and equal blame belongs to those who fail in their duty through weakness of will, which is the same as saying through shrinking from toil and pain. These cases are perfectly simple and easy to distinguish.</p>
<p class="abs about-col" style="left:622px">On the other hand, we denounce with righteous indignation and dislike men who are so beguiled and demoralized by the charms of pleasure of the moment, so blinded by desire, that they cannot foresee the pain and trouble that are bound to ensue; and equal blame belongs to those who fail in their duty through weakness of will, which is the same as saying through shrinking from toil and pain. These cases are perfectly simple and easy to distinguish.</p>
<a class="btn btn-light" style="left:532px;top:1228px;width:137px;height:40px">Read More</a>

<div class="abs van-photo" role="img" aria-label="Yellow vintage van serving drinks with a chalkboard menu, parked outdoors"></div>

<!-- What we serve -->
<div class="abs serve-bg"></div>
<div class="abs mark" style="top:2005px"></div>
<h2 class="abs section-title" style="top:2072px">WHAT WE SERVE</h2>

<div class="abs card" style="left:116px">
  <div class="card-photo" role="img" aria-label="Bartender leaning out of a trailer window" style="background:linear-gradient(135deg,#3a3a3a,#8a7a6a 50%,#c44a5a)"></div>
  <h3>Packages + Bars</h3>
  <p>Nam libero tempore, cum soluta nobis est eligendi optio cumque nihil impedit quo minus id quod maxime</p>
  <a>View Details</a>
</div>
<div class="abs card" style="left:448px">
  <div class="card-photo" role="img" aria-label="White drinks trailer with an illuminated menu board" style="background:linear-gradient(135deg,#6a5a4a,#c08a40 50%,#e8e8e8)"></div>
  <h3>Cocktail Menu</h3>
  <p>Nam libero tempore, cum soluta nobis est eligendi optio cumque nihil impedit quo minus id quod maxime</p>
  <a>View Details</a>
</div>
<div class="abs card" style="left:780px">
  <div class="card-photo" role="img" aria-label="Guests ordering at a dark green mobile bar truck" style="background:linear-gradient(135deg,#8a7a70,#3f5454 50%,#a0a4a0)"></div>
  <h3>Alcohol Calculator</h3>
  <p>Nam libero tempore, cum soluta nobis est eligendi optio cumque nihil impedit quo minus id quod maxime</p>
  <a>View Details</a>
</div>

<a class="btn btn-dark" style="left:452px;top:2707px;width:138px;height:43px">View More</a>
<a class="btn btn-outline" style="left:611px;top:2707px;width:137px;height:43px">Get Started</a>

<svg class="abs" style="left:0;top:2820px" width="1200" height="100" viewBox="0 0 1200 100" aria-hidden="true">
  <path d="M0 62 C200 10 420 0 560 20 C700 42 800 70 930 75 C1050 80 1130 60 1200 48 L1200 100 L0 100 Z" fill="#ffffff"/>
</svg>

<!-- Contact -->
<div class="abs mark" style="top:2990px"></div>
<h2 class="abs section-title" style="top:3055px">GET IN TOUCH WITH US</h2>

<div class="abs info-icon" style="top:3165px"><svg width="44" height="44" viewBox="0 0 44 44"><path d="M22 13a6 6 0 0 0-6 6c0 5 6 12 6 12s6-7 6-12a6 6 0 0 0-6-6z" fill="#fff"/><circle cx="22" cy="19" r="2.2" fill="#6b4300"/></svg></div>
<div class="abs info-title" style="top:3167px">Location</div>
<div class="abs info-text" style="top:3194px">22Y, Fern &amp; Slate, lorem lipsum is dummy<br>543 678</div>

<div class="abs info-icon" style="top:3280px"><svg width="44" height="44" viewBox="0 0 44 44"><path d="M16 14l4 0 2 5-2.5 1.5a10 10 0 0 0 4 4L25 22l5 2v4c-8 1-15-6-14-14z" fill="#fff"/></svg></div>
<div class="abs info-title" style="top:3282px">Contact Number</div>
<div class="abs info-text" style="top:3310px">+1 888 888 8888</div>

<div class="abs info-icon" style="top:3377px"><svg width="44" height="44" viewBox="0 0 44 44"><rect x="14" y="16" width="16" height="12" rx="1" fill="#fff"/><path d="M14 17l8 6 8-6" stroke="#6b4300" stroke-width="1.5" fill="none"/></svg></div>
<div class="abs info-title" style="top:3378px">Email Address</div>
<div class="abs info-text" style="top:3405px">info@fernandslate.com</div>

<div class="abs social" style="left:133px;top:3462px"><svg width="12" height="12"><circle cx="6" cy="6" r="3" fill="#6b4300"/></svg></div>
<div class="abs social" style="left:185px;top:3462px"><svg width="12" height="12"><circle cx="6" cy="6" r="3" fill="#6b4300"/></svg></div>
<div class="abs social" style="left:237px;top:3462px"><svg width="12" height="12"><circle cx="6" cy="6" r="3" fill="#6b4300"/></svg></div>

<div class="abs field" style="left:518px;top:3163px;width:259px;height:47px">First Name</div>
<div class="abs field" style="left:808px;top:3163px;width:259px;height:47px">Last Name</div>
<div class="abs field" style="left:518px;top:3230px;width:259px;height:47px">Email Address</div>
<div class="abs field" style="left:808px;top:3230px;width:259px;height:47px">Contact Number</div>
<div class="abs field" style="left:518px;top:3297px;width:549px;height:140px">Your Message Goes Here....</div>
<a class="btn btn-dark" style="left:920px;top:3463px;width:122px;height:42px">Submit Now</a>

<!-- Footer -->
<svg class="abs footer-bg" viewBox="0 0 1200 495" aria-hidden="true">
  <path d="M0 70 C150 40 300 30 450 38 C620 48 760 70 900 60 C1030 52 1120 35 1200 25 L1200 495 L0 495 Z" fill="#000000"/>
</svg>
<div class="abs brand" style="left:0;width:1200px;top:3793px;text-align:center;font-size:30px;color:var(--white)">FERN &amp; SLATE</div>
<div class="abs foot-nav" style="left:313px">Home</div>
<div class="abs foot-nav" style="left:416px">About Us</div>
<div class="abs foot-nav" style="left:541px">Our Services</div>
<div class="abs foot-nav" style="left:691px">Reviews</div>
<div class="abs foot-nav" style="left:810px">Contact Us</div>
<div class="abs social" style="left:527px;top:3950px"><svg width="12" height="12"><circle cx="6" cy="6" r="3" fill="#6b4300"/></svg></div>
<div class="abs social" style="left:579px;top:3950px"><svg width="12" height="12"><circle cx="6" cy="6" r="3" fill="#6b4300"/></svg></div>
<div class="abs social" style="left:631px;top:3950px"><svg width="12" height="12"><circle cx="6" cy="6" r="3" fill="#6b4300"/></svg></div>
<div class="abs" style="left:0;width:1200px;top:4005px;text-align:center;font-size:11.5px;color:var(--white)">© Copyright 2023 | All Rights Reserved.</div>

<div class="abs" style="left:1065px;top:3913px;width:50px;height:50px;border-radius:50%;background:var(--brown)">
  <svg width="50" height="50" viewBox="0 0 50 50"><path d="M15 18h20v12H24l-5 4v-4h-4z" fill="#fff"/></svg>
</div>

</body>
</html>
```